Menu Design Project

Bel Roux hair and beauty service menu
we need a menu to display a handful of our services to give our customers an idea of our pricing

Cutting
Ladies cuts from $35
Men's cuts from $25
All cuts are included with a wash and dry off

Velora colours
All over colours start from $55
price will vary depending upon length and thickness of hair

Foiling
starts from $50
Price will vary depending upon length of hair

Toners
from $30

Blowdries
from $35

Upstyling
wedding styling from $45
Please enquire for special occasion styling also

Beauty Services

Waxing
Eyebrow wax and shape $17.50
Lip $10
Chin/sides $20
Legs from $25
Bikini $20
XX $30
XXX $45
Back from $25
Chest from $25

Eyes
Eyebrow tinting $15
Eyelash tinting $20
Eyelash extensions from $90

Derminia facials
Express facial $45
Deluxe facial $95

Acrylic nails
full set $60
Gel polish $35
Manicures from $35
Pedicures from $45

can provide logo and other images to help

Industry/Entity Type

Hair

Requirements
Must have
• must be called a service menu
must be eye catching and memorable but not excessive
Nice to have
• postcard style size hair menu on one side
beauty menu on the other side
elegant classy design
Should not have
• must not be called a price list
stay away from traditional price list style in terms of folding out leaflet

```html
<!DOCTYPE html>
<html lang="en">
<head>
<meta charset="utf-8">
<title>Bel Roux Service Menu</title>
<link href="https://fonts.googleapis.com/css2?family=Lobster&family=Lato:ital,wght@1,300&family=Courier+Prime:wght@700&display=swap" rel="stylesheet">
<style>
  :root {
    --ink-black: #000000;
    --paper-white: #ffffff;
    --rose: #d63a8c;
    --hair-grey: #8c8c8c;
    --beauty-grey: #5a5a5a;
    --flourish-dark: #8e3566;
    --flourish-light: #e07aaf;
  }
  * { margin: 0; padding: 0; box-sizing: border-box; }
  html, body { width: 1200px; height: 829px; overflow: hidden; background: var(--paper-white); }
  .service-menu { position: relative; width: 1200px; height: 829px; display: flex; }
  .menu-side { position: relative; height: 829px; display: flex; flex-direction: column; align-items: center; }
  .menu-side--hair { width: 602px; background: var(--ink-black); color: var(--hair-grey); }
  .menu-side--beauty { width: 598px; background: var(--paper-white); color: var(--beauty-grey); }

  .menu-title {
    font-family: "Lobster", cursive;
    font-weight: 400;
    font-size: 66px;
    color: var(--rose);
    line-height: 1;
    margin-top: 62px;
  }
  .menu-subtitle {
    font-family: "Lato", sans-serif;
    font-style: italic;
    font-weight: 300;
    font-size: 44px;
    letter-spacing: -2px;
    line-height: 1;
    margin-top: 10px;
  }
  .menu-side--hair .menu-subtitle { color: #8a8a8a; }
  .menu-side--beauty .menu-subtitle { color: #6a6a6a; margin-top: 8px; }

  .service-list {
    font-family: "Courier Prime", monospace;
    font-weight: 700;
    font-variant: small-caps;
    text-align: center;
  }
  .menu-side--hair .service-list { margin-top: 38px; font-size: 15px; line-height: 19px; letter-spacing: 2px; }
  .menu-side--beauty .service-list { margin-top: 42px; font-size: 13.5px; line-height: 16px; letter-spacing: 1.5px; }
  .service-group { margin-bottom: 19px; }
  .menu-side--beauty .service-group { margin-bottom: 16px; }
  .service-group p { white-space: nowrap; }

  .flourish {
    position: absolute;
    left: 50%;
    top: 722px;
    width: 157px;
    height: 26px;
    transform: translateX(-50%);
    border-radius: 13px;
  }
  .menu-side--hair .flourish { background: var(--flourish-dark); }
  .menu-side--beauty .flourish { background: var(--flourish-light); }
</style>
</head>
<body>
<main class="service-menu">
  <section class="menu-side menu-side--hair">
    <h1 class="menu-title">Service Menu</h1>
    <h2 class="menu-subtitle">HAIR</h2>
    <div class="service-list">
      <div class="service-group">
        <p>Cutting</p>
        <p>Ladies cuts from $35</p>
        <p>Men's cuts from $25</p>
        <p>All cuts are included with a wash and dry off</p>
      </div>
      <div class="service-group">
        <p>Velora colours</p>
        <p>All over colours start from $55</p>
        <p>price will vary depending upon length and thickness of hair</p>
      </div>
      <div class="service-group">
        <p>Foiling</p>
        <p>starts from $50</p>
        <p>Price will vary depending upon length of hair</p>
      </div>
      <div class="service-group">
        <p>Toners</p>
        <p>from $30</p>
      </div>
      <div class="service-group">
        <p>Blowdries</p>
        <p>from $35</p>
        <p>price will vary depending upon length and thickness of hair</p>
      </div>
      <div class="service-group">
        <p>Upstyling</p>
        <p>wedding styling from $45</p>
        <p>Please enquire for special occasion styling also</p>
      </div>
    </div>
    <div class="flourish" role="img" aria-label="Decorative pink scroll flourish with a fleur-de-lis"></div>
  </section>

  <section class="menu-side menu-side--beauty">
    <h1 class="menu-title">Service Menu</h1>
    <h2 class="menu-subtitle">BEAUTY</h2>
    <div class="service-list">
      <div class="service-group">
        <p>Beauty Services</p>
      </div>
      <div class="service-group">
        <p>Waxing</p>
        <p>Eyebrow wax and shape $17.50</p>
        <p>Lip $10</p>
        <p>Chin/sides $20</p>
        <p>Legs from $25</p>
        <p>Bikini $20</p>
        <p>XX $30</p>
        <p>XXX $45</p>
        <p>Back from $25</p>
        <p>Chest from $25</p>
      </div>
      <div class="service-group">
        <p>Eyes</p>
        <p>Eyebrow tinting $15</p>
        <p>Eyelash tinting $20</p>
        <p>Eyelash extensions from $90</p>
      </div>
      <div class="service-group">
        <p>Derminia facials</p>
        <p>Express facial $45</p>
        <p>Deluxe facial $95</p>
      </div>
      <div class="service-group">
        <p>Acrylic nails</p>
        <p>full set $60</p>
        <p>Gel polish $35</p>
        <p>Manicures from $35</p>
        <p>Pedicures from $45</p>
      </div>
    </div>
    <div class="flourish" role="img" aria-label="Decorative light pink scroll flourish with a fleur-de-lis"></div>
  </section>
</main>
</body>
</html>
```